CBD Banner Ad for Print and Plimbo

I we would like a modern European chic that we can use in a 1/4 page ad in our local magazine and also use as our banner ad in the Plimbo ad searches. <br/><br/>We are a high end CBD boutique shop that has their own brand as well as a carefully curated selection of the top end CBD products out on the market. The final design should promote the health and well being that we are trying to live ourselves. We DO NOT want the use of marijuana paraphernalia or like substances. Think Yoga Studio meets Morvette inside of a health store. <br/><br/>Use any images you would like...I have attached a sample product render as well as the inside of our store...but take this in the direction you would like.<br/><br/>The winner will have the added bonus of being able to create 10 more ads for us in the next 6 months.

Target Market(s)

Our target market are the middle to upperclass professional workers that want to take CBD but were afraid due to misinformation or stigma

Font styles to use
Sans Serif

Colors
33b8a4
86cfc6
0792cd
3277b5
85acd3

Requirements
Must have
• A good clean modern design.
• Natural. Organic. Crisp. Welcoming.
Nice to have
• Tess Hollow
• CBD for wellness. CBD for life.
• The font we use for the rest of our campaigns is Adam.
Should not have
• Absolutely NO marijuana leaves, paraphernalia, or references. We are working hard to educate people and get rid of the stigma.

```html
<!DOCTYPE html>
<html lang="en">
<head>
<meta charset="utf-8">
<title>Tess Hollow — CBD Ad Set</title>
<link rel="stylesheet" href="https://fonts.googleapis.com/css2?family=Jost:wght@300;400&display=swap">
<style>
  :root {
    --board: #e0e0e0;
    --label: #3a3a3a;
    --paper: #f8f8f8;
    --gold: #bfa975;
    --gold-ink: #b49f66;
    --white: #ffffff;
    --teal: #33b8a4;
    --mint: #86cfc6;
    --lime: #c9e36a;
    --shop-dark: #3c3a33;
    --shop-wood: #a48b6c;
    --leaf: #3f7d3a;
  }
  html, body {
    margin: 0;
    padding: 0;
    width: 1200px;
    height: 1087px;
    overflow: hidden;
    background: var(--board);
    font-family: "Jost", sans-serif;
  }
  .board {
    position: relative;
    width: 1200px;
    height: 1087px;
  }
  .section-title {
    position: absolute;
    margin: 0;
    font-weight: 400;
    font-size: 25px;
    letter-spacing: 0.5px;
    color: var(--label);
  }
  .size-label {
    position: absolute;
    margin: 0;
    font-weight: 400;
    font-size: 17px;
    color: var(--label);
  }
  .ad { position: absolute; display: block; }
  .ad text { font-family: "Jost", sans-serif; }
  .brand-name { fill: var(--gold-ink); font-weight: 300; }
  .headline { fill: var(--white); font-weight: 300; }
  .subline { fill: var(--white); font-weight: 300; }
  .promo { fill: var(--gold-ink); font-weight: 300; }
</style>
</head>
<body>
<div class="board">

  <h2 class="section-title" style="left:138px; top:146px;">LOCAL AD</h2>
  <h2 class="section-title" style="left:629px; top:146px;">PLIMBO AD</h2>

  <!-- Print ad 15x25cm -->
  <svg class="ad ad-print" style="left:137px; top:205px;" width="420" height="701" viewBox="0 0 700 1168">
    <defs>
      <linearGradient id="printShop" x1="0" y1="0" x2="1" y2="1">
        <stop offset="0" stop-color="#e9e6e0"/>
        <stop offset="0.45" stop-color="var(--shop-wood)"/>
        <stop offset="0.75" stop-color="var(--leaf)"/>
        <stop offset="1" stop-color="var(--shop-dark)"/>
      </linearGradient>
      <linearGradient id="printGlow" x1="1" y1="0" x2="0" y2="1">
        <stop offset="0" stop-color="var(--teal)"/>
        <stop offset="0.5" stop-color="#8fd8a4"/>
        <stop offset="1" stop-color="var(--lime)"/>
      </linearGradient>
      <linearGradient id="printJars" x1="0" y1="0" x2="1" y2="1">
        <stop offset="0" stop-color="#ffffff"/>
        <stop offset="0.6" stop-color="#eef0f3"/>
        <stop offset="1" stop-color="#dcd6f0"/>
      </linearGradient>
    </defs>
    <rect width="700" height="1168" fill="var(--paper)"/>
    <polygon points="158,0 700,0 700,428 641,484" fill="url(#printShop)" role="img" aria-label="Photo of the boutique interior with shelves of products and green plants"/>
    <polygon points="700,428 700,1168 211,1168 85,1043" fill="url(#printGlow)" role="img" aria-label="Soft green and teal bokeh light backdrop"/>
    <text class="brand-name" x="62" y="300" font-size="62">Tess Hollow</text>
    <rect x="63" y="396" width="488" height="344" fill="var(--gold)"/>
    <text class="headline" x="100" y="478" font-size="44" letter-spacing="1">CBD FOR WELLNESS</text>
    <text class="headline" x="100" y="514" font-size="44" letter-spacing="1">CBD FOR LIFE</text>
    <line x1="101" y1="545" x2="259" y2="545" stroke="var(--white)" stroke-width="1.5"/>
    <text class="subline" x="100" y="600" font-size="28" letter-spacing="0.5">Huge selection of products</text>
    <text class="subline" x="100" y="630" font-size="28">www.tesshollow.shop</text>
    <rect x="92" y="683" width="432" height="348" rx="18" fill="url(#printJars)" role="img" aria-label="Product render of three supplement jars: melatonin softgels, CBD gummies and curcumin softgels"/>
    <text class="promo" transform="translate(44,1040) rotate(45)" font-size="28">CBDTESS2020</text>
    <text class="promo" transform="translate(16,1062) rotate(45)" font-size="36">20% OFF</text>
  </svg>
  <p class="size-label" style="left:138px; top:914px;">15X25CM</p>

  <!-- Web ad 336x280 -->
  <svg class="ad ad-rect" style="left:630px; top:205px;" width="202" height="168" viewBox="0 0 336 280">
    <defs>
      <linearGradient id="rectShop" x1="0" y1="0" x2="1" y2="1">
        <stop offset="0" stop-color="#e9e6e0"/>
        <stop offset="0.5" stop-color="var(--shop-wood)"/>
        <stop offset="1" stop-color="var(--leaf)"/>
      </linearGradient>
      <linearGradient id="rectGlow" x1="1" y1="0" x2="0" y2="1">
        <stop offset="0" stop-color="var(--teal)"/>
        <stop offset="1" stop-color="var(--lime)"/>
      </linearGradient>
    </defs>
    <rect width="336" height="280" fill="var(--paper)"/>
    <polygon points="145,0 336,0 336,135 270,200" fill="url(#rectShop)" role="img" aria-label="Photo of the boutique interior"/>
    <polygon points="336,135 336,280 195,280" fill="url(#rectGlow)" role="img" aria-label="Soft green bokeh backdrop"/>
    <text class="brand-name" x="28" y="60" font-size="26">Tess Hollow</text>
    <rect x="28" y="90" width="242" height="123" fill="var(--gold)"/>
    <text class="headline" x="45" y="122" font-size="21">CBD FOR WELLNESS</text>
    <text class="headline" x="45" y="141" font-size="21">CBD FOR LIFE</text>
    <line x1="45" y1="152" x2="125" y2="152" stroke="var(--white)" stroke-width="1"/>
    <rect x="60" y="165" width="180" height="97" rx="8" fill="#f1f1f3" role="img" aria-label="Row of five supplement jars"/>
  </svg>
  <p class="size-label" style="left:630px; top:383px;">336X280PX</p>

  <!-- Web ad 728x90 -->
  <svg class="ad ad-leader" style="left:630px; top:438px;" width="437" height="54" viewBox="0 0 728 90">
    <defs>
      <linearGradient id="leadShop" x1="0" y1="0" x2="1" y2="1">
        <stop offset="0" stop-color="#e9e6e0"/>
        <stop offset="0.5" stop-color="var(--shop-wood)"/>
        <stop offset="1" stop-color="var(--leaf)"/>
      </linearGradient>
      <linearGradient id="leadGlow" x1="1" y1="0" x2="0" y2="1">
        <stop offset="0" stop-color="var(--teal)"/>
        <stop offset="1" stop-color="var(--mint)"/>
      </linearGradient>
    </defs>
    <rect width="728" height="90" fill="var(--paper)"/>
    <polygon points="570,0 728,0 670,60" fill="url(#leadShop)" role="img" aria-label="Photo of the boutique interior"/>
    <polygon points="728,0 728,90 640,90" fill="url(#leadGlow)" role="img" aria-label="Soft green bokeh backdrop"/>
    <text class="brand-name" x="18" y="52" font-size="22">Tess Hollow</text>
    <rect x="163" y="0" width="345" height="90" fill="var(--gold)"/>
    <text class="headline" x="192" y="38" font-size="21">CBD FOR WELLNESS</text>
    <text class="headline" x="192" y="57" font-size="21">CBD FOR LIFE</text>
    <line x1="192" y1="67" x2="272" y2="67" stroke="var(--white)" stroke-width="1"/>
    <rect x="432" y="6" width="150" height="80" rx="6" fill="#f1f1f3" role="img" aria-label="Row of five supplement jars"/>
  </svg>
  <p class="size-label" style="left:630px; top:504px;">728X90PX</p>

</div>
</body>
</html>
```